Home Page for a Swiss based start up company, trading Natural & Health food ingredients (B2B)

I would like to create a home page for my new start up company (Valtera Swiss AG), the main field of activity is the trading and marketing of Natural and Health food ingredients towards the functional Food and Food supplements industry. (B2B).
Target Market : Functional Food and Food Supplement Manufacturers (B2B) based in Switzerland and Europe
The values I would like to convey are :
- sourcing of natural and health ingredients, (example : natural plant extracts, Omega 3, plant proteins, natural vitamins, vegan food ingredients...etc)
- Health & Nutritional Health
- Eco-friendly and Sustainability
- High Quality Standard in term of products and logistic services
- Trust and reliability
- Flexibility & speed to market
-Technical advice for the development of new products

The site will be translated in 3 languages (German, French, English)
Number of web pages : 5 : Home, About us, Products, Our Services, Contact

See here below attached Logo file.

Here some link of websites which can be taken as benchmark or source of inspiration
- https://quilbamora.com
- https://www.drevilon.com/

Target Market(s)

Manufacturers of Functional Foods and Food Supplements in Switzerland and Europe (B2B)

Industry/Entity Type

B2B Trading of Natural & Health Ingredients

Coding

Coded - Design and coding required

Number of Pages Required

5+ page

Font styles to use
Sans Serif

Colors
0054AA
0677BA
7BADD7
CADEEF
E8F1F8
0094D4
00A9DD
6FCCEA
C7EBF8
E9F6FB
00AB8E
00BBA5
67D7C9
C6EFE9
E9F9F6
59FF00
82FF00
B8FF75
E3FFCB
F4FFEA
FFF300
FFF600
FEFA6F
FFFEC7
FFFEE8
FFC000
F8CF3A
FAE287
FDF2CF
FEFAEE
F0912C
F2A743
F7CA91
FBE8D2
FDF5EE
EE7325
F08F49
F5BC92
FAE3D3
FDF4ED

Requirements
Must have
• inspiration towards nature, sustainability, vegan food, functional food & beverages, food supplements, nutritional health, low carbon footprint
Should not have
• animals, chemistry, food additives

```html
<!DOCTYPE html>
<html lang="en">
<head>
<meta charset="utf-8">
<title>Valtera Swiss AG – Natural &amp; Health Ingredients</title>
<link href="https://fonts.googleapis.com/css2?family=Montserrat:wght@600;700;800&family=Open+Sans:wght@400;600;700&display=swap" rel="stylesheet">
<style>
:root{
  --teal:#00AB8E;
  --teal-dark:#008a73;
  --teal-light:#67D7C9;
  --teal-pale:#E9F9F6;
  --teal-mist:#C6EFE9;
  --blue:#0054AA;
  --cyan:#00A9DD;
  --orange:#EE7325;
  --ink:#222;
  --text:#666;
  --footer:#1c1d1f;
  --footer-text:#c9c9c9;
  --white:#fff;
}
*{box-sizing:border-box;margin:0;padding:0}
html,body{width:1200px;height:3800px;overflow:hidden}
body{font-family:"Open Sans",Arial,sans-serif;color:var(--text);background:var(--white);position:relative}
h1,h2,h3,h4,.btn,.nav,.brand{font-family:"Montserrat",Arial,sans-serif}
.btn{display:inline-flex;align-items:center;gap:8px;background:var(--teal);color:#fff;font-weight:700;font-size:13px;letter-spacing:.5px;padding:12px 22px;border-radius:4px;text-decoration:none}
.btn svg{width:16px;height:16px}
.section-title{text-align:center;color:var(--teal);font-size:28px;font-weight:800;letter-spacing:1px}
.section-title::after{content:"";display:block;width:50px;height:3px;background:var(--teal);margin:10px auto 0;border-radius:2px}

/* top bar */
.topbar{position:absolute;top:0;left:0;width:1200px;height:44px;background:var(--teal-dark);display:flex;align-items:center;justify-content:space-between;padding:0 110px;color:#fff;font-size:13px}
.topbar .social{display:flex;gap:10px}
.topbar .social span{width:24px;height:24px;border:1px solid rgba(255,255,255,.7);border-radius:4px}
.topbar .right{display:flex;align-items:center;gap:20px}
.lang{display:flex;align-items:center;gap:6px;font-weight:600}
.lang i{width:18px;height:12px;background:#e8eef5;border-radius:2px;display:block}
.phone-pill{display:flex;align-items:center;gap:6px;background:#fff;color:var(--teal-dark);font-weight:700;padding:5px 14px;border-radius:14px;font-size:13px}
.phone-pill svg{width:13px;height:13px}

/* header */
.header{position:absolute;top:44px;left:0;width:1200px;height:68px;background:#fff;display:flex;align-items:center;padding:0 110px;box-shadow:0 2px 8px rgba(0,0,0,.06);z-index:3}
.brand{color:var(--teal);font-size:26px;font-weight:800}
.nav{display:flex;gap:30px;margin-left:auto;margin-right:36px;font-size:14px;font-weight:600;color:var(--ink)}
.nav .active{color:var(--teal);border-bottom:2px solid var(--teal);padding-bottom:4px}

/* hero */
.hero{position:absolute;top:112px;left:0;width:1200px;height:640px;overflow:hidden}
.hero-photo{position:absolute;inset:0;background:linear-gradient(180deg,#8e9aa3 0%,#b9c1c4 28%,#6f8a6a 48%,#4f7a3c 65%,#3e6a2d 100%)}
.hero-text{position:absolute;top:80px;left:0;width:100%;text-align:center;color:#fff}
.hero-text h4{font-size:20px;font-weight:700;letter-spacing:2px}
.hero-text h1{font-size:66px;font-weight:800;letter-spacing:2px;margin:4px 0 10px}
.hero-text p{font-size:16px;font-weight:600;line-height:1.5;width:560px;margin:0 auto 24px}
.arrow{position:absolute;top:270px;width:34px;height:34px;border-radius:50%;background:#fff;display:flex;align-items:center;justify-content:center}
.arrow svg{width:16px;height:16px}
.arrow.left{left:24px}.arrow.right{right:24px}
.hero-wave{position:absolute;left:0;bottom:0;width:1200px;height:200px}

/* services */
.services{position:absolute;top:752px;left:0;width:1200px;height:560px;background:linear-gradient(180deg,#fff 0%,var(--teal-pale) 100%)}
.services .section-title{margin-top:38px}
.service-cards{position:absolute;top:120px;left:130px;display:flex;gap:24px}
.card{width:218px;height:296px;border-radius:46px 8px 46px 8px;color:#fff;padding:26px 20px;text-align:center;box-shadow:0 10px 20px rgba(0,0,0,.1)}
.card.blue{background:var(--blue)}.card.cyan{background:var(--cyan)}.card.teal{background:var(--teal)}.card.orange{background:var(--orange)}
.card .icon{width:74px;height:74px;border-radius:50%;background:#fff;margin:0 auto 20px;display:flex;align-items:center;justify-content:center}
.card .icon svg{width:36px;height:36px}
.card h3{font-size:16px;font-weight:700;margin-bottom:10px}
.card p{font-size:12.5px;line-height:1.6;margin-bottom:16px}
.card .more{font-family:"Montserrat",sans-serif;font-size:12px;font-weight:700;display:inline-flex;align-items:center;gap:6px}
.card .more svg{width:13px;height:13px}

/* about */
.about{position:absolute;top:1312px;left:0;width:1200px;height:540px}
.about-drink{position:absolute;left:0;top:20px;width:470px;height:500px;background:linear-gradient(135deg,#5a2a1c 0%,#9c3d22 40%,#c77a3b 70%,#6b4a33 100%)}
.about-portrait{position:absolute;left:310px;top:130px;width:340px;height:270px;border:8px solid #fff;background:linear-gradient(160deg,#f1ede7 0%,#e3d6c8 55%,#c9b39c 100%);box-shadow:0 8px 20px rgba(0,0,0,.15)}
.about-text{position:absolute;left:650px;top:60px;width:520px}
.about-text h2{color:var(--teal);font-size:28px;font-weight:800;margin-bottom:6px}
.about-text h2::after{content:"";display:block;width:50px;height:3px;background:var(--teal);margin-top:8px}
.about-text p{font-size:13.5px;line-height:1.75;margin:18px 0 28px;text-align:justify}

/* values */
.values{position:absolute;top:1852px;left:0;width:1200px;height:880px;background:radial-gradient(circle at 50% 55%,#f5fcfb 0%,var(--teal-pale) 55%,#dff3ef 100%)}
.values .section-title{margin-top:90px}
.values-ring{position:absolute;left:350px;top:210px;width:500px;height:500px}
.globe{position:absolute;left:470px;top:330px;width:260px;height:260px;border-radius:50%;background:radial-gradient(circle at 45% 40%,#bfe9dc 0%,#5cc9a0 45%,#1f9a7a 80%,#0e7b64 100%)}
.value{position:absolute;width:240px;height:66px;background:#fff;border-radius:33px;box-shadow:0 6px 16px rgba(0,110,90,.12);display:flex;align-items:center;gap:10px;padding:0 16px}
.value.rev{flex-direction:row-reverse;text-align:right}
.value .vi{flex:none;width:44px;height:44px;border-radius:50%;background:var(--teal);display:flex;align-items:center;justify-content:center}
.value .vi svg{width:22px;height:22px}
.value h4{font-size:11.5px;font-weight:800;color:var(--ink);margin-bottom:3px}
.value p{font-size:10.5px;line-height:1.35}

/* blog */
.blog{position:absolute;top:2732px;left:0;width:1200px;height:520px}
.blog .section-title{margin-top:10px}
.posts{position:absolute;top:70px;left:110px;display:flex;gap:30px}
.post{width:320px}
.post .thumb{height:220px;border-radius:2px}
.thumb.doctor{background:linear-gradient(135deg,#e9eef0 0%,#c9d6d8 50%,#8fb38a 100%)}
.thumb.nature{background:linear-gradient(135deg,#7fa35a 0%,#4e7d35 55%,#2f5b26 100%)}
.thumb.meal{background:linear-gradient(135deg,#5a4330 0%,#b7803c 45%,#d9a55a 70%,#6d8e3b 100%)}
.post h3{font-size:13px;font-weight:800;color:var(--ink);margin:16px 0 8px}
.post h3::after{content:"";display:block;width:40px;height:3px;background:var(--teal);margin-top:8px}
.post p{font-size:12.5px;line-height:1.6}
.meta{display:flex;gap:26px;font-size:11px;color:#888;margin-top:14px;padding-top:10px;border-top:1px solid #eee}
.meta span{display:flex;align-items:center;gap:5px}
.meta svg{width:12px;height:12px}

/* footer */
.footer-wave{position:absolute;top:3220px;left:0;width:1200px;height:200px}
.footer{position:absolute;top:3400px;left:0;width:1200px;height:400px;background:var(--footer);color:var(--footer-text)}
.f-cols{position:absolute;top:20px;left:110px;display:flex;gap:100px}
.f-col h4{color:#fff;font-size:14px;font-weight:700;margin-bottom:8px}
.f-col h4::after{content:"";display:block;width:30px;height:2px;background:var(--teal);margin-top:6px}
.f-col li{list-style:none;font-size:13px;margin-top:10px;display:flex;align-items:center;gap:8px}
.f-col li::before{content:"";width:5px;height:5px;border-top:2px solid var(--teal);border-right:2px solid var(--teal);transform:rotate(45deg)}
.f-company{position:absolute;top:20px;left:860px}
.f-company h3{font-family:"Montserrat",sans-serif;color:#fff;font-size:24px;font-weight:800;margin-bottom:14px}
.f-company .addr{display:flex;gap:10px;font-size:13px;line-height:1.6}
.f-company .addr svg{width:16px;height:16px;margin-top:3px;flex:none}
.contact-bar{position:absolute;top:240px;left:140px;width:920px;height:60px;background:var(--teal);border-radius:8px;display:flex;align-items:center;justify-content:space-around}
.contact-bar .pill{display:flex;align-items:center;gap:10px;color:#fff;font-weight:700;font-size:15px}
.contact-bar .pill i{width:32px;height:32px;border-radius:50%;background:var(--teal-dark);display:flex;align-items:center;justify-content:center}
.contact-bar svg{width:15px;height:15px}
.copyright{position:absolute;bottom:18px;left:0;width:100%;text-align:center;font-size:13px;color:#aaa}
</style>
</head>
<body>

<div class="topbar">
  <div class="social"><span></span><span></span></div>
  <div class="right">
    <div class="lang"><i></i>ENG</div>
    <div class="phone-pill"><svg viewBox="0 0 24 24" fill="currentColor"><path d="M6.6 10.8a15 15 0 0 0 6.6 6.6l2.2-2.2a1 1 0 0 1 1-.25 11.4 11.4 0 0 0 3.6.57 1 1 0 0 1 1 1V20a1 1 0 0 1-1 1A17 17 0 0 1 3 4a1 1 0 0 1 1-1h3.5a1 1 0 0 1 1 1c0 1.25.2 2.45.57 3.57a1 1 0 0 1-.25 1z"/></svg>+41 44 555 0182</div>
  </div>
</div>

<header class="header">
  <div class="brand">Valtera Swiss AG</div>
  <nav class="nav"><span class="active">Home</span><span>About Us</span><span>Our Services</span><span>Our Values</span><span>Contact</span></nav>
  <a class="btn">GET STARTED <svg viewBox="0 0 24 24" fill="none" stroke="#fff" stroke-width="2.5"><circle cx="12" cy="12" r="10"/><path d="M10 8l4 4-4 4"/></svg></a>
</header>

<section class="hero">
  <div class="hero-photo" role="img" aria-label="Alpine valley with green meadows and cloudy mountain peaks"></div>
  <div class="hero-text">
    <h4>WELCOME TO</h4>
    <h1>VALTERA SWISS</h1>
    <p>Lorem ipsum dolor sit amet, consectetur adipiscing elit, sed do eiusmod tempor incididunt ut labore et dolore magna aliqua.</p>
    <a class="btn">GET STARTED <svg viewBox="0 0 24 24" fill="none" stroke="#fff" stroke-width="2.5"><circle cx="12" cy="12" r="10"/><path d="M10 8l4 4-4 4"/></svg></a>
  </div>
  <div class="arrow left"><svg viewBox="0 0 24 24" fill="none" stroke="#333" stroke-width="3"><path d="M15 5l-7 7 7 7"/></svg></div>
  <div class="arrow right"><svg viewBox="0 0 24 24" fill="none" stroke="#333" stroke-width="3"><path d="M9 5l7 7-7 7"/></svg></div>
  <svg class="hero-wave" viewBox="0 0 1200 200" preserveAspectRatio="none">
    <path d="M0 150 C260 60 520 200 760 120 C920 70 1060 30 1200 20 L1200 200 L0 200Z" fill="#00AB8E"/>
    <path d="M0 175 C280 100 540 210 800 150 C960 110 1080 80 1200 70 L1200 200 L0 200Z" fill="#67D7C9"/>
    <path d="M0 190 C300 140 560 215 820 180 C980 160 1100 140 1200 135 L1200 200 L0 200Z" fill="#fff"/>
  </svg>
</section>

<section class="services">
  <h2 class="section-title">OUR SERVICES</h2>
  <div class="service-cards">
    <div class="card blue">
      <div class="icon"><svg viewBox="0 0 24 24" fill="none" stroke="#0054AA" stroke-width="2"><circle cx="12" cy="9" r="5"/><path d="M9 13l-2 8 5-3 5 3-2-8"/></svg></div>
      <h3>Lorem Ipsum Dolor</h3>
      <p>Sit amet consectetur adipiscing elit sed do eiusmod tempor incididunt labore.</p>
      <span class="more">LEARN MORE <svg viewBox="0 0 24 24" fill="none" stroke="#fff" stroke-width="2.5"><circle cx="12" cy="12" r="10"/><path d="M10 8l4 4-4 4"/></svg></span>
    </div>
    <div class="card cyan">
      <div class="icon"><svg viewBox="0 0 24 24" fill="none" stroke="#00A9DD" stroke-width="2"><rect x="3" y="6" width="18" height="13" rx="2"/><path d="M8 6V4h8v2M12 10v5M9.5 12.5h5"/></svg></div>
      <h3>Lorem Ipsum Dolor</h3>
      <p>Sit amet consectetur adipiscing elit sed do eiusmod tempor incididunt labore.</p>
      <span class="more">LEARN MORE <svg viewBox="0 0 24 24" fill="none" stroke="#fff" stroke-width="2.5"><circle cx="12" cy="12" r="10"/><path d="M10 8l4 4-4 4"/></svg></span>
    </div>
    <div class="card teal">
      <div class="icon"><svg viewBox="0 0 24 24" fill="none" stroke="#00AB8E" stroke-width="2"><rect x="6" y="7" width="12" height="14" rx="2"/><path d="M8 3h8v4H8zM12 11v6M9 14h6"/></svg></div>
      <h3>Lorem Ipsum Dolor</h3>
      <p>Sit amet consectetur adipiscing elit sed do eiusmod tempor incididunt labore.</p>
      <span class="more">LEARN MORE <svg viewBox="0 0 24 24" fill="none" stroke="#fff" stroke-width="2.5"><circle cx="12" cy="12" r="10"/><path d="M10 8l4 4-4 4"/></svg></span>
    </div>
    <div class="card orange">
      <div class="icon"><svg viewBox="0 0 24 24" fill="none" stroke="#EE7325" stroke-width="2"><path d="M12 20s-7-4.5-7-10a4 4 0 0 1 7-2.6A4 4 0 0 1 19 10c0 5.5-7 10-7 10z"/><path d="M7 12h3l1-2 2 4 1-2h3"/></svg></div>
      <h3>Lorem Ipsum Dolor</h3>
      <p>Sit amet consectetur adipiscing elit sed do eiusmod tempor incididunt labore.</p>
      <span class="more">LEARN MORE <svg viewBox="0 0 24 24" fill="none" stroke="#fff" stroke-width="2.5"><circle cx="12" cy="12" r="10"/><path d="M10 8l4 4-4 4"/></svg></span>
    </div>
  </div>
</section>

<section class="about">
  <div class="about-drink" role="img" aria-label="Warm spiced fruit drink in a glass with cinnamon and orange slices"></div>
  <div class="about-portrait" role="img" aria-label="Smiling woman holding a dietary supplement capsule"></div>
  <div class="about-text">
    <h2>ABOUT US</h2>
    <p>Sed ut perspiciatis unde omnis iste natus error sit voluptatem accusantium doloremque laudantium, totam rem aperiam, eaque ipsa quae ab illo inventore veritatis et quasi architecto beatae vitae dicta sunt explicabo. Nemo enim ipsam voluptatem quia voluptas sit aspernatur aut odit aut fugit, sed quia consequuntur magni dolores eos qui ratione voluptatem sequi nesciunt. Neque porro quisquam est, qui dolorem ipsum quia dolor sit amet, consectetur, adipisci velit, sed quia non numquam eius modi tempora incidunt ut labore et dolore magnam aliquam quaerat voluptatem. Ut enim ad minima veniam, quis nostrum exercitationem.</p>
    <a class="btn">MORE ABOUT US <svg viewBox="0 0 24 24" fill="none" stroke="#fff" stroke-width="2.5"><circle cx="12" cy="12" r="10"/><path d="M10 8l4 4-4 4"/></svg></a>
  </div>
</section>

<section class="values">
  <h2 class="section-title">OUR VALUES</h2>
  <svg class="values-ring" viewBox="0 0 500 500">
    <circle cx="250" cy="250" r="230" fill="none" stroke="#00AB8E" stroke-width="2" stroke-dasharray="3 7"/>
    <circle cx="250" cy="250" r="175" fill="#fff" stroke="#67D7C9" stroke-width="6"/>
    <g fill="#00AB8E">
      <circle cx="250" cy="20" r="6"/><circle cx="250" cy="480" r="6"/>
      <circle cx="20" cy="250" r="6"/><circle cx="480" cy="250" r="6"/>
      <circle cx="87" cy="87" r="6"/><circle cx="413" cy="87" r="6"/>
      <circle cx="87" cy="413" r="6"/><circle cx="413" cy="413" r="6"/>
    </g>
  </svg>
  <div class="globe" role="img" aria-label="Green globe with a young plant sprouting on top"></div>

  <div class="value" style="left:480px;top:170px"><div class="vi"><svg viewBox="0 0 24 24" fill="none" stroke="#fff" stroke-width="2"><path d="M5 19c0-8 6-13 14-14-1 8-6 14-14 14zM5 19l7-7"/></svg></div><div><h4>HEALTH INGREDIENTS</h4><p>Lorem ipsum dolor sit amet consectetur adipiscing</p></div></div>
  <div class="value rev" style="left:90px;top:290px"><div class="vi"><svg viewBox="0 0 24 24" fill="none" stroke="#fff" stroke-width="2"><path d="M3 12l4-4 5 3 5-3 4 4-9 7z"/></svg></div><div><h4>TRUST AND RELIABILITY</h4><p>Lorem ipsum dolor sit amet consectetur adipiscing</p></div></div>
  <div class="value" style="left:870px;top:290px"><div class="vi"><svg viewBox="0 0 24 24" fill="none" stroke="#fff" stroke-width="2"><path d="M12 20s-7-4.5-7-10a4 4 0 0 1 7-2.6A4 4 0 0 1 19 10c0 5.5-7 10-7 10z"/></svg></div><div><h4>NUTRITIONAL HEALTH</h4><p>Lorem ipsum dolor sit amet consectetur adipiscing</p></div></div>
  <div class="value rev" style="left:50px;top:420px"><div class="vi"><svg viewBox="0 0 24 24" fill="none" stroke="#fff" stroke-width="2"><path d="M4 12h16M14 6l6 6-6 6M10 6l-6 6 6 6"/></svg></div><div><h4>FLEXIBILITY</h4><p>Lorem ipsum dolor sit amet consectetur adipiscing</p></div></div>
  <div class="value" style="left:910px;top:420px"><div class="vi"><svg viewBox="0 0 24 24" fill="none" stroke="#fff" stroke-width="2"><path d="M20 12a8 8 0 1 1-3-6.2M20 4v5h-5"/></svg></div><div><h4>ECO-FRIENDLY</h4><p>Lorem ipsum dolor sit amet consectetur adipiscing</p></div></div>
  <div class="value rev" style="left:90px;top:550px"><div class="vi"><svg viewBox="0 0 24 24" fill="none" stroke="#fff" stroke-width="2"><path d="M5 19l6-6M14 4l6 6-4 4-6-6zM4 4l5 5M15 15l5 5"/></svg></div><div><h4>TECHNICAL ADVICE</h4><p>Lorem ipsum dolor sit amet consectetur adipiscing</p></div></div>
  <div class="value" style="left:870px;top:550px"><div class="vi"><svg viewBox="0 0 24 24" fill="none" stroke="#fff" stroke-width="2"><circle cx="12" cy="12" r="8"/><path d="M8 12l3 3 5-6"/></svg></div><div><h4>HIGH QUALITY</h4><p>Lorem ipsum dolor sit amet consectetur adipiscing</p></div></div>
  <div class="value rev" style="left:480px;top:720px"><div class="vi"><svg viewBox="0 0 24 24" fill="none" stroke="#fff" stroke-width="2"><path d="M12 3l7 3v6c0 4-3 7-7 9-4-2-7-5-7-9V6z"/></svg></div><div><h4>SECURITY OF SUPPLY</h4><p>Lorem ipsum dolor sit amet consectetur adipiscing</p></div></div>
</section>

<section class="blog">
  <h2 class="section-title">LATEST BLOG</h2>
  <div class="posts">
    <article class="post">
      <div class="thumb doctor" role="img" aria-label="Nutritionist at a desk with fresh vegetables advising a client"></div>
      <h3>LOREM IPSUM DOLOR SIT AMET, CONSE</h3>
      <p>Lorem ipsum dolor sit amet, consectetur adipiscing elit sed do eiusmod tempor incididunt ut labore et dolore.</p>
      <div class="meta"><span><svg viewBox="0 0 24 24" fill="none" stroke="#00AB8E" stroke-width="2"><rect x="3" y="5" width="18" height="16" rx="2"/><path d="M3 10h18M8 3v4M16 3v4"/></svg>Sep 01 , 2021</span><span><svg viewBox="0 0 24 24" fill="none" stroke="#00AB8E" stroke-width="2"><path d="M4 5h16v11H8l-4 4z"/></svg>No Comments</span></div>
    </article>
    <article class="post">
      <div class="thumb nature" role="img" aria-label="Hands holding a green sprout with sustainability symbols"></div>
      <h3>LOREM IPSUM DOLOR SIT AMET, CONSE</h3>
      <p>Lorem ipsum dolor sit amet, consectetur adipiscing elit sed do eiusmod tempor incididunt ut labore et dolore.</p>
      <div class="meta"><span><svg viewBox="0 0 24 24" fill="none" stroke="#00AB8E" stroke-width="2"><rect x="3" y="5" width="18" height="16" rx="2"/><path d="M3 10h18M8 3v4M16 3v4"/></svg>Sep 01 , 2021</span><span><svg viewBox="0 0 24 24" fill="none" stroke="#00AB8E" stroke-width="2"><path d="M4 5h16v11H8l-4 4z"/></svg>No Comments</span></div>
    </article>
    <article class="post">
      <div class="thumb meal" role="img" aria-label="Healthy vegan bowls with grains and vegetables on a wooden table"></div>
      <h3>LOREM IPSUM DOLOR SIT AMET, CONSE</h3>
      <p>Lorem ipsum dolor sit amet, consectetur adipiscing elit sed do eiusmod tempor incididunt ut labore et dolore.</p>
      <div class="meta"><span><svg viewBox="0 0 24 24" fill="none" stroke="#00AB8E" stroke-width="2"><rect x="3" y="5" width="18" height="16" rx="2"/><path d="M3 10h18M8 3v4M16 3v4"/></svg>Sep 01 , 2021</span><span><svg viewBox="0 0 24 24" fill="none" stroke="#00AB8E" stroke-width="2"><path d="M4 5h16v11H8l-4 4z"/></svg>No Comments</span></div>
    </article>
  </div>
</section>

<svg class="footer-wave" viewBox="0 0 1200 200" preserveAspectRatio="none">
  <path d="M0 40 C250 0 450 130 700 110 C900 95 1050 30 1200 50 L1200 200 L0 200Z" fill="#00AB8E"/>
  <path d="M0 80 C260 40 480 170 720 150 C920 130 1060 70 1200 90 L1200 200 L0 200Z" fill="#1c1d1f"/>
</svg>

<footer class="footer">
  <div class="f-cols">
    <div class="f-col"><h4>QUICK LINKS</h4><ul><li>Home</li><li>About Us</li><li>Our Services</li></ul></div>
    <div class="f-col"><h4>OTHER LINKS</h4><ul><li>Terms Of Use</li><li>Privacy Policy</li><li>FAQ</li></ul></div>
    <div class="f-col"><h4>USEFUL LINKS</h4><ul><li>Our Values</li><li>Help Service</li><li>Contact Us</li></ul></div>
  </div>
  <div class="f-company">
    <h3>Valtera Swiss AG</h3>
    <div class="addr"><svg viewBox="0 0 24 24" fill="#00AB8E"><path d="M12 2a7 7 0 0 0-7 7c0 5 7 13 7 13s7-8 7-13a7 7 0 0 0-7-7zm0 9.5A2.5 2.5 0 1 1 12 6.5a2.5 2.5 0 0 1 0 5z"/></svg><span>27 Lindenweg<br>8004 Zürich</span></div>
  </div>
  <div class="contact-bar">
    <div class="pill"><i><svg viewBox="0 0 24 24" fill="#fff"><path d="M6.6 10.8a15 15 0 0 0 6.6 6.6l2.2-2.2a1 1 0 0 1 1-.25 11.4 11.4 0 0 0 3.6.57 1 1 0 0 1 1 1V20a1 1 0 0 1-1 1A17 17 0 0 1 3 4a1 1 0 0 1 1-1h3.5a1 1 0 0 1 1 1c0 1.25.2 2.45.57 3.57a1 1 0 0 1-.25 1z"/></svg></i>+41 44 555 0182</div>
    <div class="pill"><i><svg viewBox="0 0 24 24" fill="#fff"><path d="M6.6 10.8a15 15 0 0 0 6.6 6.6l2.2-2.2a1 1 0 0 1 1-.25 11.4 11.4 0 0 0 3.6.57 1 1 0 0 1 1 1V20a1 1 0 0 1-1 1A17 17 0 0 1 3 4a1 1 0 0 1 1-1h3.5a1 1 0 0 1 1 1c0 1.25.2 2.45.57 3.57a1 1 0 0 1-.25 1z"/></svg></i>+41 44 555 0297</div>
    <div class="pill"><i><svg viewBox="0 0 24 24" fill="none" stroke="#fff" stroke-width="2"><rect x="3" y="5" width="18" height="14" rx="2"/><path d="M3 7l9 6 9-6"/></svg></i>info@valteraswiss.com</div>
  </div>
  <div class="copyright">© 2021 Valtera Swiss. All Rights Reserved</div>
</footer>

</body>
</html>
```